International Legal Service Company needs Letterhead Design

Put my new Logo into Letterhead Design, using updated telephone number, e-mail address and website. Current letterhead and updated information which i want you to include my new letterhead attached herewith. Of course, my new Logo attached herein. Also, you can use slogan "Total Legal Outsourcing Solutions For Multinational Businesses"

It Company

```html
<!DOCTYPE html>
<html lang="en">
<head>
<meta charset="utf-8">
<title>Meridian Counsel Partners Inc — Letterhead</title>
<link rel="stylesheet" href="https://fonts.googleapis.com/css2?family=Open+Sans:wght@600&family=Roboto+Condensed:wght@400;700&display=swap">
<style>
  :root {
    --paper: #ffffff;
    --brand-blue: #2b4889;
    --brand-mid: #3f6fb8;
    --footer-text: #ffffff;
  }
  * { margin: 0; padding: 0; box-sizing: border-box; }
  html, body {
    width: 942px;
    height: 1200px;
    overflow: hidden;
    background: var(--paper);
  }
  .letterhead {
    position: relative;
    width: 942px;
    height: 1200px;
    background: var(--paper);
    font-family: "Open Sans", Arial, sans-serif;
  }
  .brand {
    position: absolute;
    left: 74px;
    top: 66px;
    display: flex;
    align-items: center;
    gap: 14px;
  }
  .brand-mark {
    width: 86px;
    height: 86px;
    border-radius: 50%;
    background: var(--brand-mid);
    flex: none;
  }
  .brand-name {
    font-size: 25px;
    font-weight: 600;
    color: var(--brand-blue);
    line-height: 1.2;
    letter-spacing: -0.2px;
  }
  .footer-band {
    position: absolute;
    left: 0;
    top: 1130px;
    width: 942px;
    height: 48px;
    background: var(--brand-blue);
  }
  .footer-mark {
    position: absolute;
    left: 62px;
    top: 1092px;
    width: 124px;
    height: 124px;
    border-radius: 50%;
    background: var(--paper);
    display: flex;
    align-items: center;
    justify-content: center;
  }
  .footer-mark span {
    width: 88px;
    height: 88px;
    border-radius: 50%;
    background: var(--brand-mid);
  }
  .footer-details {
    position: absolute;
    left: 226px;
    top: 1136px;
    width: 690px;
    font-family: "Roboto Condensed", "Arial Narrow", sans-serif;
    font-size: 11.5px;
    line-height: 19px;
    letter-spacing: 0.8px;
    color: var(--footer-text);
    text-transform: uppercase;
    white-space: nowrap;
  }
  .footer-details strong { font-weight: 700; }
</style>
</head>
<body>
  <main class="letterhead">
    <header class="brand">
      <div class="brand-mark" aria-hidden="true"></div>
      <p class="brand-name">Meridian Counsel<br>Partners Inc</p>
    </header>

    <div class="footer-band"></div>
    <div class="footer-mark" aria-hidden="true"><span></span></div>
    <footer class="footer-details">
      <p><strong>Meridian Counsel</strong> Partners Inc | 1480 Harbor Point Drive, Suite 300, Easton, MD 21601</p>
      <p><strong>Phn.</strong> 410.555.0148 | <strong>Fax.</strong> 410.555.0193 | <strong>Email.</strong> jd@meridiancp.com | <strong>Web.</strong> meridiancp.com</p>
    </footer>
  </main>
</body>
</html>
```